bargainmentor.net - Podcast Guest Marketing E-Flyer PDF

Dear Designers:I am in need of an attractive and attention-getting layout and design for a three-page marketing flyer (commonly known as a media one sheet) that will be sent via e-mail, as PDF file, to various Podcast hosts to market me as a guest on their podcasts. I want the design of the document to "mirror" the design and branding on my parent bargainmentor.net website. I am providing ALL the edited and proofread copy and content - the designer just needs to create the design for this marketing document. I want an active PDF document and icons should be used for LinkedIn, Phone, E-mail , and website- with hyperlinks that connect accordingly. I need a fast turnaround.
Updates

Dear Designers - instead of using the photo in the project file of me speaking to the audience for the banner image - I thought it would be a better idea to make this marketing piece specific to Podcast Hosts. Therefore, an image such as the one in the link below would be good to use for a banner image. https://www.pixtrove-example.net/gallery?topic=recording+booth+images&ref=qz7&view=grid&id=Kx93LmPwa2RtVbN8YcQdE4&w=1377&h=804#pic=vRmalqobet:

Target Market(s)

This PDF document will be sent to 650 Podcast hosts in North America via a broadcast e-mail.

Font styles to use
Sans Serif

Colors
ec1f27
ffffff
000000
333333
9d9d9d

Requirements
Must have
• A three-page layout that is easy to navigate in PDF form.
• Proper font styles and sizes for key emphasis areas on the document/
• Consistent branding to mirror my bargainmentor.net parent website
• Must be easy for people to read
• Attention-getting design elements and layout
• Professional and sophisticated design
• Icons for contact information
Should not have
• Should not be cluttered and junky-looking.
• Should not use small font sizes that makes it difficult to read.
• If Podcast hosts are interested in having me as a guest - they will read the content as required on three-pages

```html
<!DOCTYPE html>
<html lang="en">
<head>
<meta charset="utf-8">
<title>Bargain Mentor – Podcast Guest One Sheet</title>
<link href="https://fonts.googleapis.com/css2?family=Lato:ital,wght@0,300;0,400;0,700;0,900;1,400;1,700&display=swap" rel="stylesheet">
<style>
  :root{
    --red:#ec1f27;
    --white:#ffffff;
    --black:#000000;
    --ink:#333333;
    --grey:#9d9d9d;
  }
  *{margin:0;padding:0;box-sizing:border-box}
  html,body{width:960px;height:1200px;overflow:hidden;background:var(--white)}
  body{font-family:"Lato",sans-serif;color:var(--ink)}
  .sheet{position:relative;width:960px;height:1200px;background:var(--white)}

  .title-panel{position:absolute;left:87px;top:0;width:298px;height:342px;background:var(--red);color:var(--white);padding:112px 0 0 39px}
  .title-panel .kicker{font-weight:300;font-size:22px;line-height:26px}
  .title-panel h1{font-weight:900;font-size:22px;line-height:26px;text-transform:uppercase;letter-spacing:-.2px}
  .title-panel h1 span{display:block;margin-top:6px}

  .feature-quote{position:absolute;left:430px;top:62px;width:470px;text-align:center}
  .quote-mark{display:block;margin:0 auto}
  .feature-quote p{font-size:13.5px;line-height:16px;color:var(--ink);margin-top:18px}
  .feature-quote cite{display:block;font-style:italic;font-size:11px;line-height:14px;margin:14px 0 12px;color:var(--ink)}

  .event-band{position:absolute;left:0;top:342px;width:960px;height:358px}
  .studio-photo{position:absolute;inset:0;background:radial-gradient(ellipse at 62% 55%,#3a3a3a 0%,#1a1a1a 35%,#050505 75%)}
  .event-content{position:absolute;left:97px;top:44px;width:800px;color:var(--white)}
  .event-content .lead{font-weight:300;font-size:22px;line-height:27px}
  .event-content .lead strong{display:block;color:var(--red);font-weight:700}
  .event-content ul{list-style:none;margin-top:30px}
  .event-content li{font-size:13.5px;line-height:16px;margin-bottom:17px}

  .host-block{position:absolute;left:87px;top:700px;width:298px}
  .host-block .cap{height:51px;background:var(--red)}
  .host-block .details{padding:31px 0 0 25px;font-size:15px;line-height:23px}
  .host-block .name{font-weight:700;color:var(--black)}
  .host-block .org{font-style:italic;color:var(--red)}
  .host-block .role{color:var(--black);margin-top:2px}
  .host-block .rule{position:absolute;left:0;top:214px;width:298px;height:12px;background:var(--red)}

  .brand-mark{position:absolute;left:535px;top:770px;width:340px;text-align:center}
  .brand-mark .square{width:70px;height:70px;background:var(--red);margin:0 auto 18px}
  .brand-mark .wordmark{font-size:42px;font-weight:400;color:var(--black);letter-spacing:-.5px}

  .book-line{position:absolute;left:0;top:1047px;width:960px;text-align:center;font-style:italic;font-weight:700;font-size:24px;color:var(--red)}

  .contact-bar{position:absolute;left:0;top:1086px;width:960px;height:51px;background:var(--black);color:var(--white);font-size:15px}
  .contact{position:absolute;top:12px;display:flex;align-items:center;gap:12px}
  .contact svg{flex:none}
  .contact.email{left:88px}
  .contact.phone{left:364px}
  .contact.phone span{font-weight:700}
  .contact.profile{left:598px}

  .site-link{position:absolute;left:233px;top:1137px;width:496px;height:48px;border:2px solid var(--red);border-top:none;text-align:center;font-weight:900;font-size:23px;line-height:46px;color:var(--black)}
</style>
</head>
<body>
<main class="sheet">
  <section class="title-panel">
    <p class="kicker">Testimonials:</p>
    <h1>What some<br>clients are<br>saying about<span>The Bargain<br>Mentor®</span></h1>
  </section>

  <section class="feature-quote">
    <svg class="quote-mark" width="52" height="40" viewBox="0 0 52 40" aria-hidden="true"><g fill="var(--red)"><circle cx="12" cy="28" r="12"/><path d="M2 26 Q4 6 20 2 L21 6 Q12 10 11 20 Z"/><circle cx="38" cy="28" r="12"/><path d="M28 26 Q30 6 46 2 L47 6 Q38 10 37 20 Z"/></g></svg>
    <p>Daniel Harwick did a terrific job on my podcast. His negotiating insights and tips were well received by my listeners, and he was an engaging, knowledgeable, and entertaining guest. Given my expertise in real estate, I thought I was a good negotiator– until Daniel taught me a few new strategies and tips during the podcast. I would recommend Daniel to any podcast host –he is a pro and his topics are relevant and can benefit everyone.</p>
    <cite>-Carl Brenner, Podcast Host Property Growth Forum Podcast,<br>San Antonio, Texas</cite>
    <svg class="quote-mark" width="52" height="40" viewBox="0 0 52 40" aria-hidden="true"><g fill="var(--red)" transform="rotate(180 26 20)"><circle cx="12" cy="28" r="12"/><path d="M2 26 Q4 6 20 2 L21 6 Q12 10 11 20 Z"/><circle cx="38" cy="28" r="12"/><path d="M28 26 Q30 6 46 2 L47 6 Q38 10 37 20 Z"/></g></svg>
  </section>

  <section class="event-band">
    <div class="studio-photo" role="img" aria-label="Dark podcast studio photo with a microphone on a stand"></div>
    <div class="event-content">
      <p class="lead">Below is a partial listing of testimonials from attendees at an <strong>Founders' Alliance (FA) event provided by the RT Halvorsen, Chapter Learning Chair:</strong></p>
      <ul>
        <li>“A very engaging, entertaining, and inspirational speaker who provided very useful information, strategies, and tips to apply to all my future negotiations.”</li>
        <li>“Thank you to FA Western New York for booking this speaker! I learned some things that I can address immediately and a lot material that I need to practice. Great session!”</li>
        <li>“Daniel was an outstanding speaker on the topic of negotiating! He was one of my favorite speakers ever! Daniel was a real ‘teacher’ versus other typical speakers who spend two hours bragging or promoting their book.”</li>
        <li>“Daniel was a very knowledgeable and well-prepared speaker who provided helpful tips and scripts throughout the entire presentation! I would love to learn more from this speaker.”</li>
      </ul>
    </div>
  </section>

  <section class="host-block">
    <div class="cap"></div>
    <div class="details">
      <p class="name">RT Halvorsen, CEO and President</p>
      <p class="org">Meridian Records Group</p>
      <p class="org">Founders' Alliance (FA)</p>
      <p class="org">Western New York</p>
      <p class="role">Learning Chair</p>
    </div>
    <div class="rule"></div>
  </section>

  <div class="brand-mark">
    <div class="square"></div>
    <p class="wordmark">bargainmentor</p>
  </div>

  <p class="book-line">Book Bargain Mentor® Daniel R. Harwick for Your Podcast</p>

  <footer class="contact-bar">
    <a class="contact email">
      <svg width="28" height="28" viewBox="0 0 28 28" aria-hidden="true"><circle cx="14" cy="14" r="13" fill="none" stroke="var(--red)" stroke-width="2"/><rect x="7" y="9" width="14" height="10" fill="var(--red)"/><path d="M7 9 L14 15 L21 9" fill="none" stroke="var(--black)" stroke-width="1.5"/></svg>
      <span>daniel@harwickmail.net</span>
    </a>
    <a class="contact phone">
      <svg width="28" height="28" viewBox="0 0 28 28" aria-hidden="true"><circle cx="14" cy="14" r="13" fill="none" stroke="var(--red)" stroke-width="2"/><path d="M10 7 L13 10 L11.5 12.5 Q13 16 16 17 L18 15 L21 18 L19 21 Q11 21 7 10 Z" fill="var(--red)"/></svg>
      <span>555-204-7719</span>
    </a>
    <a class="contact profile">
      <svg width="28" height="28" viewBox="0 0 28 28" aria-hidden="true"><circle cx="14" cy="14" r="13" fill="none" stroke="var(--red)" stroke-width="2"/></svg>
      <span>netprofile.net/in/danielharwick</span>
    </a>
  </footer>

  <a class="site-link">WWW.BARGAINMENTOR.NET</a>
</main>
</body>
</html>
```